Redesign for Popular UK Town Website

We're looking for someone to redesign a website for a popular tourist town that's visited by over 250,000 people a year. We have a basic design frame in place and need someone to make it look more 'professional.'
We've created a temporary design layout to show you a general idea of what we're looking for: http://dorrin.co.uk/
All text/images are placeholder images so you can get an idea of the general layout.
(Please note that you can grab any images found on the internet for 'tenby' to be used as placeholder images. This is because we will be visiting the locations and taking our own photos, after the design is complete.)
Target Market(s)
Tourists
Industry/Entity Type
Town
Number of Pages Required
2 page
Requirements
Must have
- You need to redesign the homepage: http://dorrin.co.uk/
- You also need to redesign the following page: http://dorrin.co.uk/hotels/ (This page will be used for multiple categories and is used to list locations of properties/places etc.)
- Design must be responsive also.
Nice to have
- Please feel free to add as much as you can to the content/features as with our limited knowledge of websites, have only been able to create a basic layout.

```html
<!DOCTYPE html>
<html lang="en">
<head>
<meta charset="utf-8">
<title>Dorrin Hotels</title>
<link href="https://fonts.googleapis.com/css2?family=Open+Sans:wght@400;600;700&display=swap" rel="stylesheet">
<style>
:root{
  --navy:#0d3a5c;
  --navy-deep:#0b3452;
  --cyan:#1aa7e0;
  --text:#3a3a3a;
  --muted:#8a8a8a;
  --card:#f3f3f3;
  --white:#ffffff;
  --yellow:#f4d21c;
  --footer-text:#c8d6e2;
}
*{box-sizing:border-box;margin:0;padding:0}
html,body{width:739px;height:1200px;overflow:hidden}
body{position:relative;background:var(--white);font-family:'Open Sans',sans-serif;color:var(--text)}
.site-header{position:absolute;left:0;top:0;width:739px;height:34px;background:var(--white)}
.brand{position:absolute;left:132px;top:5px;display:flex;align-items:center;gap:5px;color:var(--navy);font-weight:700;font-size:14px}
.brand-dot{width:22px;height:22px;border-radius:50%;background:var(--navy)}
.main-nav span{position:absolute;top:13px;font-size:6px;line-height:8px;color:var(--navy);white-space:nowrap;letter-spacing:.1px}
.nav-1{left:238px}.nav-2{left:297px}.nav-3{left:382px}.nav-4{left:456px}
.search-icon{position:absolute;left:522px;top:11px}
.weather{position:absolute;left:547px;top:0;width:63px;height:34px;background:var(--cyan);color:var(--white);text-align:center;font-weight:700}
.weather-label{font-size:8px;padding-top:4px}
.weather-temp{font-size:11px;line-height:14px}
.weather-temp small{font-size:6.5px;font-weight:400;margin-right:3px}
.title-band{position:absolute;left:0;top:34px;width:739px;height:44px;background:var(--navy)}
.page-title{position:absolute;right:129px;top:12px;font-size:15.5px;font-weight:700;color:var(--white)}
.intro{position:absolute;left:130px;top:100px;width:480px;text-align:center;font-size:8px;line-height:13px;color:var(--muted)}
.listing{position:absolute;left:130px;top:154px;width:480px;display:grid;grid-template-columns:repeat(3,152px);column-gap:12px;row-gap:15px}
.hotel-card{height:174px;background:var(--card)}
.hotel-photo{height:87px}
.tone-a{background:linear-gradient(180deg,#c9d4d0,#7a9b8e)}
.tone-b{background:linear-gradient(180deg,#eef0f2,#a8aaa6)}
.tone-c{background:linear-gradient(180deg,#f1f2f3,#c2c4c3)}
.tone-d{background:linear-gradient(180deg,#d6dbd2,#7b8d74)}
.tone-e{background:linear-gradient(180deg,#3a63a8,#c4c7cb)}
.tone-f{background:linear-gradient(180deg,#7aa2d8,#e9d68a)}
.hotel-name{margin:6px 0 0 6px;font-size:8.5px;font-weight:700;color:var(--cyan);text-transform:uppercase}
.contact{display:flex;align-items:center;gap:5px;margin:4px 0 0 5px;height:14px;font-size:7px;color:var(--text);white-space:nowrap}
.contact.phone{font-size:11px;font-weight:600;margin-top:6px}
.contact svg{flex:none}
.slider-arrow{position:absolute;top:712px}
.slider-arrow.prev{left:92px}
.slider-arrow.next{left:603px}
.load-more{position:absolute;left:329px;top:913px;width:59px;height:19px;border:1px solid var(--cyan);border-radius:3px;font-size:7px;color:var(--cyan);display:flex;align-items:center;justify-content:center;letter-spacing:.3px}
.site-footer{position:absolute;left:0;top:970px;width:739px;height:230px;background:var(--navy-deep);color:var(--footer-text)}
.social{position:absolute;left:339px;top:18px;display:flex;gap:4px}
.social span{width:19px;height:19px;border-radius:2px;background:#3d6686}
.footer-nav{position:absolute;left:0;top:51px;width:739px;text-align:center;font-size:6.5px;letter-spacing:.2px}
.footer-rule{position:absolute;left:130px;top:69px;width:480px;height:1px;background:#3b6180}
.footer-col{position:absolute;top:92px;font-size:6px}
.footer-col h4{font-size:6.8px;font-weight:700;color:var(--white);margin-bottom:8px;text-transform:uppercase}
.footer-col li{list-style:none;line-height:11.2px}
.col-1{left:130px}.col-2{left:234px}.col-3{left:346px}.col-4{left:440px}
.subscribe{display:flex;margin-top:6px}
.subscribe-input{width:92px;height:19px;background:var(--white);color:#999;font-size:6px;padding:5px 6px}
.subscribe-btn{width:40px;height:19px;background:var(--yellow);color:var(--navy);font-size:6px;font-weight:700;display:flex;align-items:center;justify-content:center}
.footer-brand{position:absolute;left:0;top:185px;width:739px;display:flex;justify-content:center;align-items:center;gap:4px;font-size:12px;font-weight:700;color:#2c587a}
.footer-brand span{width:16px;height:16px;border-radius:50%;background:#2c587a}
.copyright{position:absolute;left:0;top:213px;width:739px;text-align:center;font-size:5px;color:#4e7391}
</style>
</head>
<body>
<svg width="0" height="0" style="position:absolute">
  <defs>
    <symbol id="i-phone" viewBox="0 0 16 16"><circle cx="8" cy="8" r="7" fill="none" stroke="#1f3f5c" stroke-width="1.4"/><path d="M5.2 4.3l1.5-.3.8 2-1 .8c.5 1.1 1.3 1.9 2.4 2.4l.8-1 2 .8-.3 1.5c-3.3.3-6.5-2.9-6.2-6.2z" fill="#1f3f5c"/></symbol>
    <symbol id="i-mail" viewBox="0 0 16 16"><circle cx="8" cy="8" r="7.5" fill="#1f3f5c"/><rect x="4" y="5.2" width="8" height="5.6" rx=".6" fill="#fff"/><path d="M4.2 5.5L8 8.3l3.8-2.8" fill="none" stroke="#1f3f5c" stroke-width=".9"/></symbol>
    <symbol id="i-web" viewBox="0 0 16 16"><circle cx="8" cy="8" r="7.5" fill="#1f3f5c"/><circle cx="8" cy="8" r="4" fill="none" stroke="#fff" stroke-width=".9"/><path d="M4 8h8M8 4c-1.6 2.4-1.6 5.6 0 8M8 4c1.6 2.4 1.6 5.6 0 8" fill="none" stroke="#fff" stroke-width=".8"/></symbol>
  </defs>
</svg>

<header class="site-header">
  <div class="brand"><span class="brand-dot"></span>Dorrin</div>
  <nav class="main-nav"><span class="nav-1">WHERE TO STAY</span><span class="nav-2">CARAVAN AND CAMPING</span><span class="nav-3">BED AND BREAKFAST</span><span class="nav-4">HOTELS IN DORRIN</span></nav>
  <svg class="search-icon" width="12" height="12" viewBox="0 0 14 14"><circle cx="6" cy="6" r="4.5" fill="none" stroke="#b9b9b9" stroke-width="1.4"/><path d="M9.3 9.3L13 13" stroke="#b9b9b9" stroke-width="1.6"/></svg>
  <div class="weather"><div class="weather-label">WEATHER</div><div class="weather-temp"><small>TODAY</small>6°C</div></div>
</header>

<section class="title-band"><h1 class="page-title">Dorrin Hotels</h1></section>

<p class="intro">Most famous for it's Harbourlight Hotel, Dorrin actually has over 18 hotels with availability throughout the year. All information for the hotels listed below are valid as of March 2018. To make a booking enquiry, please contact the hotels directly.</p>

<main class="listing">
  <article class="hotel-card"><div class="hotel-photo tone-a" role="img" aria-label="Photo of the Harbourlight Hotel frontage"></div><h2 class="hotel-name">Harbourlight Hotel</h2><p class="contact phone"><svg width="13" height="13"><use href="#i-phone"/></svg>01234 560186</p><p class="contact"><svg width="13" height="13"><use href="#i-mail"/></svg>stay@harbourlight-hotel.co.uk</p><p class="contact"><svg width="13" height="13"><use href="#i-web"/></svg>http://www.harbourlight-hotel.co.uk/</p></article>
  <article class="hotel-card"><div class="hotel-photo tone-b" role="img" aria-label="Photo of The Terrace Hotel entrance"></div><h2 class="hotel-name">The Terrace Hotel</h2><p class="contact phone"><svg width="13" height="13"><use href="#i-phone"/></svg>01234 560248</p><p class="contact"><svg width="13" height="13"><use href="#i-mail"/></svg>hello@terracehoteldorrin.com</p><p class="contact"><svg width="13" height="13"><use href="#i-web"/></svg>http://terracehoteldorrin.com/</p></article>
  <article class="hotel-card"><div class="hotel-photo tone-c" role="img" aria-label="Photo of The Cliff Walk Hotel facade"></div><h2 class="hotel-name">The Cliff Walk Hotel</h2><p class="contact phone"><svg width="13" height="13"><use href="#i-phone"/></svg>01234 560186</p><p class="contact"><svg width="13" height="13"><use href="#i-mail"/></svg>01234 560333</p><p class="contact"><svg width="13" height="13"><use href="#i-web"/></svg>http://www.thecliffwalkhotel.com/</p></article>

  <article class="hotel-card"><div class="hotel-photo tone-d" role="img" aria-label="Photo of Seaview House Hotel frontage"></div><h2 class="hotel-name">Seaview House Hotel</h2><p class="contact phone"><svg width="13" height="13"><use href="#i-phone"/></svg>01234 560371</p><p class="contact"><svg width="13" height="13"><use href="#i-mail"/></svg>info@seaviewhouse-dorrin.co.uk</p><p class="contact"><svg width="13" height="13"><use href="#i-web"/></svg>www.seaviewhouse-dorrin.co.uk/</p></article>
  <article class="hotel-card"><div class="hotel-photo tone-e" role="img" aria-label="Photo of The Westgate Hotel building"></div><h2 class="hotel-name">The Westgate Hotel</h2><p class="contact phone"><svg width="13" height="13"><use href="#i-phone"/></svg>01234 560698</p><p class="contact"><svg width="13" height="13"><use href="#i-mail"/></svg>westgatehotel@mailbox.com</p><p class="contact"><svg width="13" height="13"><use href="#i-web"/></svg>http://thewestgatehotel.com/</p></article>
  <article class="hotel-card"><div class="hotel-photo tone-f" role="img" aria-label="Photo of the Breakwater Hotel building"></div><h2 class="hotel-name">Breakwater Hotel</h2><p class="contact phone"><svg width="13" height="13"><use href="#i-phone"/></svg>01234 560881</p><p class="contact"><svg width="13" height="13"><use href="#i-mail"/></svg>enquiries@breakwater-hotel.co.uk</p><p class="contact"><svg width="13" height="13"><use href="#i-web"/></svg>www.breakwater-hotel.co.uk/</p></article>

  <article class="hotel-card"><div class="hotel-photo tone-a" role="img" aria-label="Photo of the Harbourlight Hotel frontage"></div><h2 class="hotel-name">Harbourlight Hotel</h2><p class="contact phone"><svg width="13" height="13"><use href="#i-phone"/></svg>01234 560186</p><p class="contact"><svg width="13" height="13"><use href="#i-mail"/></svg>stay@harbourlight-hotel.co.uk</p><p class="contact"><svg width="13" height="13"><use href="#i-web"/></svg>http://www.harbourlight-hotel.co.uk/</p></article>
  <article class="hotel-card"><div class="hotel-photo tone-b" role="img" aria-label="Photo of The Terrace Hotel entrance"></div><h2 class="hotel-name">The Terrace Hotel</h2><p class="contact phone"><svg width="13" height="13"><use href="#i-phone"/></svg>01234 560248</p><p class="contact"><svg width="13" height="13"><use href="#i-mail"/></svg>hello@terracehoteldorrin.com</p><p class="contact"><svg width="13" height="13"><use href="#i-web"/></svg>http://terracehoteldorrin.com/</p></article>
  <article class="hotel-card"><div class="hotel-photo tone-c" role="img" aria-label="Photo of The Cliff Walk Hotel facade"></div><h2 class="hotel-name">The Cliff Walk Hotel</h2><p class="contact phone"><svg width="13" height="13"><use href="#i-phone"/></svg>01234 560186</p><p class="contact"><svg width="13" height="13"><use href="#i-mail"/></svg>01234 560333</p><p class="contact"><svg width="13" height="13"><use href="#i-web"/></svg>http://www.thecliffwalkhotel.com/</p></article>

  <article class="hotel-card"><div class="hotel-photo tone-d" role="img" aria-label="Photo of Seaview House Hotel frontage"></div><h2 class="hotel-name">Seaview House Hotel</h2><p class="contact phone"><svg width="13" height="13"><use href="#i-phone"/></svg>01234 560371</p><p class="contact"><svg width="13" height="13"><use href="#i-mail"/></svg>info@seaviewhouse-dorrin.co.uk</p><p class="contact"><svg width="13" height="13"><use href="#i-web"/></svg>www.seaviewhouse-dorrin.co.uk/</p></article>
  <article class="hotel-card"><div class="hotel-photo tone-e" role="img" aria-label="Photo of The Westgate Hotel building"></div><h2 class="hotel-name">The Westgate Hotel</h2><p class="contact phone"><svg width="13" height="13"><use href="#i-phone"/></svg>01234 560698</p><p class="contact"><svg width="13" height="13"><use href="#i-mail"/></svg>westgatehotel@mailbox.com</p><p class="contact"><svg width="13" height="13"><use href="#i-web"/></svg>http://thewestgatehotel.com/</p></article>
  <article class="hotel-card"><div class="hotel-photo tone-f" role="img" aria-label="Photo of the Breakwater Hotel building"></div><h2 class="hotel-name">Breakwater Hotel</h2><p class="contact phone"><svg width="13" height="13"><use href="#i-phone"/></svg>01234 560881</p><p class="contact"><svg width="13" height="13"><use href="#i-mail"/></svg>enquiries@breakwater-hotel.co.uk</p><p class="contact"><svg width="13" height="13"><use href="#i-web"/></svg>www.breakwater-hotel.co.uk/</p></article>
</main>

<svg class="slider-arrow prev" width="12" height="20" viewBox="0 0 12 20"><path d="M10 2L2 10l8 8" fill="none" stroke="#d4d4d4" stroke-width="1.6"/></svg>
<svg class="slider-arrow next" width="12" height="20" viewBox="0 0 12 20"><path d="M2 2l8 8-8 8" fill="none" stroke="#d4d4d4" stroke-width="1.6"/></svg>

<div class="load-more">LOAD MORE</div>

<footer class="site-footer">
  <div class="social"><span></span><span></span><span></span><span></span></div>
  <p class="footer-nav">WHERE TO STAY &nbsp;•&nbsp; CARAVAN AND CAMPING &nbsp;•&nbsp; BED AND BREAKFAST &nbsp;•&nbsp; HOTELS IN DORRIN</p>
  <div class="footer-rule"></div>
  <div class="footer-col col-1"><h4>Top Hotels in Dorrin</h4><ul><li>Rosebay House Hotel</li><li>Brookfield Boutique B&amp;B</li><li>Hollins Hotel</li><li>Breakwater Hotel</li><li>The Terrace Hotel Dorrin</li><li>Marlow Spa Hotel</li></ul></div>
  <div class="footer-col col-2"><h4>Top Places in Dorrin</h4><ul><li>Harbour Beach</li><li>Dorrin Lifeboat Station</li><li>Greenacre World of Activities</li><li>Penhallow Castle</li><li>Old Merchant's House</li><li>Eastcliff Castle</li></ul></div>
  <div class="footer-col col-3"><h4>Dorrin Nearby</h4><ul><li>Larkin Island</li><li>Seaspray Water Park</li><li>Dorrin Car Parks</li><li>Meadow Farm</li><li>Anchor Pub</li></ul></div>
  <div class="footer-col col-4"><h4>Subscribe Newsletter</h4><p>Get latest updates via email directly in your inbox</p><div class="subscribe"><div class="subscribe-input">Enter your email address</div><div class="subscribe-btn">SUBSCRIBE</div></div></div>
  <div class="footer-brand"><span></span>Dorrin</div>
  <p class="copyright">Copyright © 2018 Dorrin Visitor Guide. All rights reserved.</p>
</footer>
</body>
</html>
```